Brightwell Wiring Needs A Logo Design

We need a logo for my new company based out of Sacramento, Ca called Brightwell Wiring. The name says it all, my electrical contracting business provides "Brightwell Craftsman Work" I'm open to any colors that pop and customers to say Wow. I would love to print my cards on metal.

Contact Information for Business Card

The card needs to have as follows
Name of company: Brightwell Wiring
My Name: Marco Delvane
Phone # 916-555-0147
CL# 4873920
Email: brightwellwiring@mailtorva.com
and a slogan that represent "BRIGHTWELL"

Requirements
Must have
• The card needs to have as follows
• Name of company: Brightwell Wiring
• My Name : Marco Delvane
• Phone # 916-555-0147
• CL# 4873920
• Email: brightwellwiring@mailtorva.com
• and a slogan that represent "BRIGHTWELL"
Nice to have
• popping colors
• electrical Arcing

```html
<!DOCTYPE html>
<html lang="en">
<head>
<meta charset="utf-8">
<title>Brightwell Wiring – Business Card</title>
<link rel="stylesheet" href="https://fonts.googleapis.com/css2?family=Roboto+Slab:wght@700&family=Open+Sans:wght@400;700&display=swap">
<style>
  :root {
    --page-bg: #2b2927;
    --card-top: #050608;
    --card-bottom: #1b1c1e;
    --brand-blue: #1d84cc;
    --band-blue: #1a7fc6;
    --band-text: #0a1a2b;
    --body-grey: #c9c9c9;
    --muted-grey: #a8a8a8;
    --arc-glow: #3a3f9e;
  }
  * { margin: 0; padding: 0; box-sizing: border-box; }
  html, body {
    width: 1200px; height: 1200px; overflow: hidden;
    background: var(--page-bg);
  }
  .card {
    position: absolute; left: 100px; top: 314px;
    width: 1000px; height: 572px;
    background: var(--card-bottom);
    overflow: hidden;
    box-shadow: 0 10px 30px rgba(0,0,0,.5);
  }
  .card__top {
    position: absolute; left: 0; top: 0; width: 100%; height: 300px;
    background: var(--card-top);
  }
  .card__arc-art {
    position: absolute; right: 0; top: 0; width: 470px; height: 345px;
    background: radial-gradient(ellipse at 85% 35%, #c9ccff 0%, #5a5fd0 12%, var(--arc-glow) 30%, #12142e 60%, var(--card-top) 85%);
  }
  .brand {
    position: absolute; left: 70px; top: 120px;
    display: flex; align-items: center; gap: 18px;
  }
  .brand__mark {
    width: 44px; height: 44px; background: var(--brand-blue);
  }
  .brand__name {
    font-family: "Roboto Slab", serif; font-weight: 700;
    font-size: 54px; color: var(--brand-blue); letter-spacing: .5px;
  }
  .slogan-band {
    position: absolute; left: 0; top: 300px; width: 100%; height: 46px;
    background: var(--band-blue);
    display: flex; align-items: center; justify-content: center;
    padding-left: 230px;
  }
  .slogan-band__text {
    font-family: "Open Sans", sans-serif; font-weight: 700;
    font-size: 24px; color: var(--band-text); letter-spacing: .5px;
  }
  .owner {
    position: absolute; left: 70px; top: 366px;
  }
  .owner__name {
    font-family: "Roboto Slab", serif; font-weight: 700;
    font-size: 40px; color: var(--brand-blue); line-height: 1.1;
  }
  .owner__title {
    font-family: "Open Sans", sans-serif; font-size: 24px;
    color: var(--muted-grey); margin-top: 4px;
  }
  .divider {
    position: absolute; left: 480px; top: 400px; width: 2px; height: 150px;
    background: var(--brand-blue);
  }
  .contact {
    position: absolute; left: 515px; top: 425px;
    list-style: none;
    font-family: "Open Sans", sans-serif; font-size: 26px; color: var(--body-grey);
  }
  .contact__item { display: flex; align-items: center; gap: 14px; height: 40px; }
  .contact__icon { width: 26px; height: 26px; flex: none; }
  .contact__label { color: var(--brand-blue); font-weight: 700; }
</style>
</head>
<body>
  <div class="card">
    <div class="card__top"></div>
    <div class="card__arc-art" role="img" aria-label="Photograph of electrical arcs and lightning bolts on a dark sky"></div>

    <div class="brand">
      <span class="brand__mark"></span>
      <span class="brand__name">Brightwell Wiring</span>
    </div>

    <div class="slogan-band">
      <span class="slogan-band__text">BRIGHTWELL CRAFTSMAN WORK</span>
    </div>

    <div class="owner">
      <p class="owner__name">MARCO DELVANE</p>
      <p class="owner__title">OWNER</p>
    </div>

    <div class="divider"></div>

    <ul class="contact">
      <li class="contact__item">
        <svg class="contact__icon" viewBox="0 0 24 24"><rect width="24" height="24" rx="4" fill="#1d84cc"/><path d="M8 5.5l2.3 3-1.4 1.6c.9 1.9 2.4 3.4 4.3 4.3l1.6-1.4 3 2.3-1.5 2.4c-5.2-.4-10.1-5.3-10.5-10.5z" fill="#1b1c1e"/></svg>
        <span>916-555-0147</span>
      </li>
      <li class="contact__item">
        <svg class="contact__icon" viewBox="0 0 24 24"><rect width="24" height="24" rx="4" fill="#1d84cc"/><rect x="5" y="7.5" width="14" height="9.5" fill="#1b1c1e"/><path d="M5 7.5l7 5.5 7-5.5" stroke="#1d84cc" stroke-width="1.5" fill="none"/></svg>
        <span>brightwellwiring@mailtorva.com</span>
      </li>
      <li class="contact__item">
        <span class="contact__label">CL#</span>
        <span>4873920</span>
      </li>
    </ul>
  </div>
</body>
</html>
```